Can Design for Fun, Growing Health Food Brand

We are launching a brand new product, electrolyte seltzer drinks. We want the design to be clean/simple and slightly modern while staying true to our brand identity. Must say "Mineral Hydration" as the product descriptor, sub headline is "Carbonated electrolyte beverage with sea moss and real fruit juice". First flavors will be Watermelon Mint and Mango.

Target Market(s)

Women ages 30-50 who are interested in health wellness/trends

Industry/Entity Type

Health & Wellness

Font styles to use
Sans Serif

Requirements
Must have
• Tall, skinny can, current Bright Kelp Co Logo, use aluminum on can as element in design.
Nice to have
• Be fun, clean and modern. Would like to see the label less busy than our gels.
Should not have
• Avoid putting flavor on bottom 1/5 of can. No gradient color changes. Do not want really detailed or realistic fruit image, prefer drawings or similar.

```html
<!DOCTYPE html>
<html lang="en">
<head>
<meta charset="utf-8">
<title>Bright Kelp Co — Mineral Hydration Can Labels</title>
<link rel="stylesheet" href="https://fonts.googleapis.com/css2?family=Montserrat:wght@800&family=Oswald:wght@400;500&display=swap">
<style>
  :root {
    --page: #ececec;
    --aluminum: #b3b3b3;
    --frame: #333333;
    --mango: #ffcc00;
    --watermelon-mint: #006837;
    --ink-white: #ffffff;
  }
  html, body {
    margin: 0;
    padding: 0;
    width: 685px;
    height: 1200px;
    overflow: hidden;
    background: var(--page);
  }
  .canvas {
    position: relative;
    width: 685px;
    height: 1200px;
  }
  .can-label {
    position: absolute;
    left: 134px;
    width: 416px;
    height: 560px;
    display: block;
  }
  .can-label--mango { top: 30px; --flavor: var(--mango); }
  .can-label--watermelon-mint { top: 610px; --flavor: var(--watermelon-mint); }
  .label-ground { fill: var(--aluminum); stroke: var(--frame); stroke-width: 2; }
  .flavor-field { fill: var(--flavor); }
  .brand-mark { fill: none; stroke: var(--ink-white); stroke-width: 3; }
  .brand-name {
    font-family: "Oswald", sans-serif;
    font-weight: 400;
    font-size: 34px;
    fill: var(--ink-white);
  }
  .descriptor {
    font-family: "Montserrat", sans-serif;
    font-weight: 800;
    font-size: 108px;
    fill: var(--ink-white);
  }
  .flavor-name {
    font-family: "Montserrat", sans-serif;
    font-weight: 800;
    font-size: 30px;
    fill: var(--ink-white);
  }
  .subheadline {
    font-family: "Oswald", sans-serif;
    font-weight: 500;
    font-size: 25px;
    fill: var(--ink-white);
  }
</style>
</head>
<body>
<main class="canvas">

  <svg class="can-label can-label--mango" viewBox="0 0 661 889" aria-label="Mango can label">
    <rect class="label-ground" x="1" y="1" width="659" height="887"/>
    <rect class="flavor-field" x="160" y="2" width="340" height="885" role="img" aria-label="Flowing mango-yellow swoosh with silver stripes and bubbles"/>
    <circle class="brand-mark" cx="334" cy="59" r="21"/>
    <text class="brand-name" x="334" y="127" text-anchor="middle">BRIGHT KELP CO</text>
    <text class="flavor-name" transform="translate(258,398) rotate(-90)" textLength="120" lengthAdjust="spacingAndGlyphs">MANGO</text>
    <text class="descriptor" transform="translate(313,823) rotate(-90)" textLength="340" lengthAdjust="spacingAndGlyphs">MINERAL</text>
    <text class="descriptor" transform="translate(410,823) rotate(-90)" textLength="515" lengthAdjust="spacingAndGlyphs">HYDRATION</text>
    <text class="subheadline" transform="translate(450,823) rotate(-90)" textLength="515" lengthAdjust="spacingAndGlyphs">CARBONATED ELECTROLYTE BEVERAGE WITH SEA MOSS AND REAL FRUIT JUICE</text>
  </svg>

  <svg class="can-label can-label--watermelon-mint" viewBox="0 0 661 889" aria-label="Watermelon Mint can label">
    <rect class="label-ground" x="1" y="1" width="659" height="887"/>
    <rect class="flavor-field" x="160" y="2" width="340" height="885" role="img" aria-label="Flowing green swoosh with silver stripes and bubbles"/>
    <circle class="brand-mark" cx="334" cy="59" r="21"/>
    <text class="brand-name" x="334" y="127" text-anchor="middle">BRIGHT KELP CO</text>
    <text class="flavor-name" transform="translate(256,398) rotate(-90)" textLength="200" lengthAdjust="spacingAndGlyphs">WATERMELON</text>
    <text class="flavor-name" transform="translate(283,398) rotate(-90)" textLength="82" lengthAdjust="spacingAndGlyphs">MINT</text>
    <text class="descriptor" transform="translate(313,823) rotate(-90)" textLength="340" lengthAdjust="spacingAndGlyphs">MINERAL</text>
    <text class="descriptor" transform="translate(410,823) rotate(-90)" textLength="515" lengthAdjust="spacingAndGlyphs">HYDRATION</text>
    <text class="subheadline" transform="translate(450,823) rotate(-90)" textLength="515" lengthAdjust="spacingAndGlyphs">CARBONATED ELECTROLYTE BEVERAGE WITH SEA MOSS AND REAL FRUIT JUICE</text>
  </svg>

</main>
</body>
</html>
```